Admin Backend Redesign

We need a redesign for our backend which supoosed to make the backoffice look more modern!

I will add screenshots of the backoffice so you know what data will be shown in the Admin.

Have in mind that the users of this backend are Doctors. We need a clinical look, modern and sharp. The backoffice is responsive, have that in mind. We need the backoffice to look as professional as possible.

The theme used for the website is: http://velmora.brisk-sample.net/

ON the main page of the backoffice, under every widget i need some space to write an explanation what the widget is about.

The color code used in our logo and website is #57aad4 combined with white.

We are open for ideas!
Updates

Project Deadline Extended
Reason: Designs are ok, but nothing innovative. Please use more modern designs!

Project Deadline Extended
Reason: Havent recieved a perfect design yet. Please read instructions carefully! Thank you

Project Deadline Extended
Reason: Hey everybody, sorry for the delay. We will decide in 3 days. If anyone wants to add a Design, that would be great.

Target Market(s)

Doctors, therapists

Industry/Entity Type

It Professional

Font styles to use
Sans Serif

Requirements
Must have
• Must look uptodate, modern, like new back offices look nowadays

```html
<!DOCTYPE html>
<html lang="de">
<head>
<meta charset="utf-8">
<title>Medical Admin Dashboard</title>
<link href="https://fonts.googleapis.com/css2?family=Open+Sans:wght@300;400;600;700&display=swap" rel="stylesheet">
<style>
  :root{
    --brand:#57aad4;
    --brand-deep:#1f6fb2;
    --brand-mid:#2c84c4;
    --banner:#29a3dd;
    --banner-strip:#1f8fcf;
    --panel:#f3f4f8;
    --panel-edge:#d7dbe2;
    --ink:#4a5866;
    --ink-soft:#6c7782;
    --ink-faint:#9aa3ab;
    --green:#7fb241;
    --green-btn:#5cb85c;
    --blue-series:#6ba3bd;
    --red:#fb4b5c;
    --grey-ring:#e6e6e6;
    --white:#ffffff;
  }
  *{box-sizing:border-box;margin:0;padding:0}
  html,body{width:1200px;height:1138px;overflow:hidden;background:var(--white);font-family:"Open Sans",Arial,sans-serif;color:var(--ink)}
  .canvas{position:relative;width:1200px;height:1138px}

  .topbar{position:absolute;left:0;top:0;width:1200px;height:34px;background:linear-gradient(90deg,#1d5f9e,#2e86c5 60%,#3a95cf)}
  .user{position:absolute;right:38px;top:7px;display:flex;align-items:center;gap:6px;color:var(--white);font-size:10px}
  .user .avatar{width:20px;height:20px;background:linear-gradient(#dde3e8,#9aa6b0);border:1px solid #fff}

  .sidebar{position:absolute;left:0;top:34px;width:161px;height:1104px;background:linear-gradient(180deg,#2676bb,#3c93cc 60%,#4ea3d6)}
  .menu-toggle{position:absolute;left:126px;top:10px;width:20px;height:20px;background:#4aa3dc;display:flex;flex-direction:column;justify-content:center;align-items:center;gap:2px}
  .menu-toggle span{display:block;width:10px;height:1px;background:#fff}
  .nav{position:absolute;left:0;top:50px;width:161px;list-style:none}
  .nav li{height:29px;display:flex;align-items:center;padding-left:12px;gap:7px;color:var(--white);font-size:10.5px;border-bottom:1px solid rgba(255,255,255,.12);position:relative}
  .nav li.active{background:rgba(255,255,255,.18)}
  .nav li.active::after{content:"";position:absolute;right:-6px;top:9px;border:6px solid transparent;border-left:6px solid rgba(255,255,255,.18);border-right:0}
  .nav .chev{position:absolute;right:12px;font-size:11px}
  .nav svg{width:13px;height:13px;fill:#fff}

  .page-title{position:absolute;left:176px;top:48px;font-size:23px;font-weight:300;color:var(--brand)}
  .page-title small{font-size:10px;color:var(--ink-soft);margin-left:4px}
  .breadcrumb{position:absolute;left:183px;top:91px;font-size:10.5px;color:var(--ink);display:flex;gap:6px;align-items:center}
  .breadcrumb .current{color:var(--brand)}

  .banner{position:absolute;top:128px;height:82px;background:var(--banner);overflow:hidden;color:var(--white)}
  .banner .photo{position:absolute;left:0;top:0;height:65px;background:linear-gradient(90deg,#1c6ea8,#3a8fc6 50%,#5aa9d8 80%,rgba(41,163,221,0))}
  .banner .label{position:absolute;right:9px;top:10px;text-align:right}
  .banner .label h2{font-size:24px;font-weight:300;line-height:1.1}
  .banner .label p{font-size:12px;font-weight:300}
  .banner .strip{position:absolute;left:0;bottom:0;width:100%;height:17px;background:var(--banner-strip);font-size:7.5px;padding:0 14px;display:flex;align-items:center;justify-content:space-between;text-transform:uppercase}
  .banner .strip svg{width:10px;height:10px}

  .panel{position:absolute;background:var(--panel);border-left:2px solid var(--panel-edge)}
  .panel-title{position:absolute;left:28px;top:22px;font-size:13.5px;font-weight:600;color:var(--ink);display:flex;align-items:center;gap:8px}
  .panel-title svg{width:11px;height:10px}
  .panel p{position:absolute;left:27px;top:59px;width:448px;font-size:12.2px;line-height:17px;color:var(--ink-soft)}
  .btn{position:absolute;left:26px;top:216px;width:62px;height:24px;background:var(--green-btn);color:#fff;font-size:10.5px;display:flex;align-items:center;justify-content:center}
  .panel svg.chart{position:absolute;left:0;top:0}

  .legend{position:absolute;left:226px;top:130px;display:flex;gap:14px}
  .legend .item{text-align:center;font-size:10px;color:var(--ink)}
  .legend .item b{font-weight:400;display:flex;align-items:center;gap:4px}
  .legend .item i{display:inline-block;width:12px;height:12px;border-radius:50%}
  .legend .item span{display:block;font-size:8px;color:var(--ink-faint);margin-top:3px}

  .table-head{position:absolute;top:793px;display:flex;align-items:center;justify-content:space-between}
  .table-head h3{font-size:12px;font-weight:400;color:var(--ink);display:flex;align-items:center;gap:5px}
  .grid-icon{display:grid;grid-template-columns:repeat(3,3px);gap:1px}
  .grid-icon i{width:3px;height:3px;background:#b6a13b}
  .entries{width:117px;height:23px;border:1px solid #d7dadf;display:flex;font-size:8.5px;color:var(--ink);background:#fff}
  .entries span:first-child{flex:1;display:flex;align-items:center;padding-left:9px;border-right:1px solid #d7dadf}
  .entries span:last-child{width:34px;display:flex;align-items:center;justify-content:center;gap:4px;color:var(--ink-faint)}

  .data-table{position:absolute;top:826px;border-collapse:collapse;background:#fff;box-shadow:0 1px 3px rgba(0,0,0,.18);font-size:9px;color:var(--ink)}
  .data-table th{height:26px;text-align:left;font-weight:400;background:linear-gradient(#f7f7f7,#ececec);border-bottom:1px solid #dcdcdc}
  .data-table td{height:33px}
  .data-table tr:nth-child(even) td{background:var(--panel)}
  .data-table th:first-child,.data-table td:first-child{padding-left:27px}
  .data-table th span{font-size:7px;margin-left:4px}

  .pager{position:absolute;top:1035px;display:flex;border:1px solid #d7dadf;background:#fff}
  .pager span{width:20px;height:20px;display:flex;align-items:center;justify-content:center;font-size:9px;color:var(--brand-mid);border-left:1px solid #d7dadf}
  .pager span:first-child{border-left:0;width:30px}
  .pager span:last-child{width:30px}
  .pager span.on{background:#e5e5e5;color:var(--ink)}

  .footer{position:absolute;left:183px;top:1115px;font-size:9px;color:var(--ink-faint)}
</style>
</head>
<body>
<div class="canvas">

  <header class="topbar">
    <div class="user"><div class="avatar" role="img" aria-label="Profilfoto des Benutzers"></div>Dr. John Doe <span style="opacity:.5;font-size:8px">&#8964;</span></div>
  </header>

  <aside class="sidebar">
    <div class="menu-toggle"><span></span><span></span><span></span></div>
    <ul class="nav">
      <li class="active"><svg viewBox="0 0 16 16"><path d="M8 1 1 8h2v7h4v-5h2v5h4V8h2z"/></svg>Dashboard</li>
      <li><svg viewBox="0 0 16 16"><circle cx="8" cy="5" r="4"/><path d="M0 16c0-5 4-6 8-6s8 1 8 6z"/></svg>Mein Konto<span class="chev">&rsaquo;</span></li>
      <li><svg viewBox="0 0 20 16"><circle cx="10" cy="5" r="3.5"/><circle cx="4" cy="6" r="2.5"/><circle cx="16" cy="6" r="2.5"/><path d="M3 16c0-4 3-6 7-6s7 2 7 6zM0 14c0-3 2-4 4-4l-1 4zM20 14c0-3-2-4-4-4l1 4z"/></svg>Patientenbewetungen<span class="chev">&rsaquo;</span></li>
    </ul>
  </aside>

  <h1 class="page-title">Dashboard<small>Welcome to Medical Application</small></h1>
  <div class="breadcrumb">
    <svg width="10" height="9" viewBox="0 0 16 16" fill="#4a5866"><path d="M8 1 1 8h2v7h4v-5h2v5h4V8h2z"/></svg>
    <span>Home</span><span>&rsaquo;</span><span class="current">Dashboard</span>
  </div>

  <section class="banner" style="left:176px;width:488px">
    <div class="photo" style="width:360px" role="img" aria-label="Gruppenfoto des medizinischen Teams"></div>
    <div class="label"><h2>Profil</h2><p>Profil bearbeiten</p></div>
    <div class="strip">Weiter<svg viewBox="0 0 12 12" fill="none" stroke="#fff"><circle cx="6" cy="6" r="5"/><path d="M3.5 6h5M6.5 4l2 2-2 2"/></svg></div>
  </section>
  <section class="banner" style="left:685px;width:489px">
    <div class="photo" style="width:270px" role="img" aria-label="Foto einer Patientenfamilie"></div>
    <div class="label"><h2>Patienten</h2><p>Patienten verwalten</p></div>
    <div class="strip">Alle ansehen<svg viewBox="0 0 12 12" fill="none" stroke="#fff"><circle cx="6" cy="6" r="5"/><path d="M3.5 6h5M6.5 4l2 2-2 2"/></svg></div>
  </section>

  <section class="panel" style="left:176px;top:228px;width:488px;height:260px">
    <h2 class="panel-title"><svg viewBox="0 0 11 10" fill="none" stroke="#8a939b"><rect x=".5" y=".5" width="10" height="9"/><path d="M3 8V5M5.5 8V3M8 8V6"/></svg>Willkommen: Dr.Mustermann</h2>
    <p>It is a long established fact that a reader will be distracted by the readable content of a page when looking at its layout. The point of using Lorem Ipsum is that it has a more-or-less normal distribution of letters, as opposed to using 'Content here, content here', making it look like readable English. Many desktop publishing packages and web page editors now use Lorem Ipsum as their default model text, and a search for 'lorem ipsum' will uncover many web sites still in their infancy.</p>
    <div class="btn">Button</div>
  </section>

  <section class="panel" style="left:685px;top:228px;width:489px;height:260px">
    <h2 class="panel-title"><svg viewBox="0 0 11 10" fill="none" stroke="#8a939b"><rect x=".5" y=".5" width="10" height="9"/><path d="M3 8V5M5.5 8V3M8 8V6"/></svg>Nerova Trend Fur:</h2>
    <svg class="chart" width="489" height="260" viewBox="0 0 521 278" font-family="Open Sans, sans-serif" font-size="10" fill="#4a5866">
      <g stroke="#e2e4ea">
        <line x1="56" y1="67" x2="390" y2="67"/><line x1="56" y1="96" x2="390" y2="96"/><line x1="56" y1="125" x2="390" y2="125"/><line x1="56" y1="154" x2="390" y2="154"/><line x1="56" y1="183" x2="390" y2="183"/>
        <line x1="76" y1="60" x2="76" y2="215"/><line x1="124" y1="60" x2="124" y2="215"/><line x1="172" y1="60" x2="172" y2="215"/><line x1="220" y1="60" x2="220" y2="215"/><line x1="268" y1="60" x2="268" y2="215"/><line x1="316" y1="60" x2="316" y2="215"/><line x1="364" y1="60" x2="364" y2="215"/>
        <line x1="50" y1="215" x2="390" y2="215" stroke="#cfd3da"/>
      </g>
      <g text-anchor="end"><text x="43" y="71">100</text><text x="43" y="100">80</text><text x="43" y="129">60</text><text x="43" y="158">40</text><text x="43" y="187">20</text></g>
      <g text-anchor="middle"><text x="78" y="230">2007</text><text x="128" y="230">2008</text><text x="178" y="230">2009</text><text x="229" y="230">2010</text><text x="282" y="230">2011</text><text x="332" y="230">2012</text></g>
      <polygon points="76,215 76,152 124,102 172,122 220,110 268,85 316,130 364,106 364,215" fill="#e4ead6" opacity=".8"/>
      <polygon points="76,215 76,204 124,183 172,135 220,178 268,169 316,194 364,179 364,215" fill="#dde6ee" opacity=".9"/>
      <polyline points="76,152 124,102 172,122 220,110 268,85 316,130 364,106" fill="none" stroke="#8db64e" stroke-width="2"/>
      <polyline points="76,204 124,183 172,135 220,178 268,169 316,194 364,179" fill="none" stroke="#6fa5bf" stroke-width="2"/>
      <g fill="#fff" stroke="#8db64e" stroke-width="2"><circle cx="76" cy="152" r="3.5"/><circle cx="124" cy="102" r="3.5"/><circle cx="172" cy="122" r="3.5"/><circle cx="268" cy="85" r="3.5"/><circle cx="316" cy="130" r="3.5"/><circle cx="364" cy="106" r="3.5"/></g>
      <circle cx="220" cy="110" r="5.5" fill="#6a9f2f"/>
      <g fill="#fff" stroke="#6fa5bf" stroke-width="2"><circle cx="76" cy="204" r="3.5"/><circle cx="124" cy="183" r="3.5"/><circle cx="172" cy="135" r="3.5"/><circle cx="220" cy="178" r="3.5"/><circle cx="268" cy="169" r="3.5"/><circle cx="316" cy="194" r="3.5"/><circle cx="364" cy="179" r="3.5"/></g>
      <rect x="203" y="66" width="34" height="21" rx="2" fill="#5f6870"/><path d="M216 87h8l-4 4z" fill="#5f6870"/>
      <text x="220" y="81" text-anchor="middle" fill="#fff" font-size="9">+14</text>
    </svg>
  </section>

  <section class="panel" style="left:176px;top:509px;width:488px;height:261px">
    <h2 class="panel-title"><svg viewBox="0 0 11 10" fill="none" stroke="#8a939b"><rect x=".5" y=".5" width="10" height="9"/><path d="M3 8V5M5.5 8V3M8 8V6"/></svg>Pie 1</h2>
    <svg class="chart" width="200" height="261" viewBox="0 0 213 278">
      <g transform="rotate(-90 121 155)" fill="none">
        <circle cx="121" cy="155" r="66.5" stroke="#e6e6e6" stroke-width="31" stroke-dasharray="87.7 417.8" stroke-dashoffset="-330.1"/>
        <circle cx="121" cy="155" r="66.5" stroke="#fb4b5c" stroke-width="31" stroke-dasharray="58.5 417.8" stroke-dashoffset="-271.6"/>
        <circle cx="121" cy="155" r="66.5" stroke="#5e9ab8" stroke-width="31" stroke-dasharray="104.5 417.8" stroke-dashoffset="-167.1"/>
        <circle cx="121" cy="155" r="68" stroke="#7fb241" stroke-width="34" stroke-dasharray="167.1 427.3"/>
      </g>
    </svg>
    <div class="legend">
      <div class="item"><b><i style="background:var(--green)"></i>40%</b><span>Visits</span></div>
      <div class="item"><b><i style="background:var(--blue-series)"></i>25%</b><span>Sales</span></div>
      <div class="item"><b><i style="background:var(--red)"></i>14%</b><span>Members</span></div>
    </div>
  </section>

  <section class="panel" style="left:685px;top:509px;width:489px;height:261px">
    <h2 class="panel-title"><svg viewBox="0 0 11 10" fill="none" stroke="#8a939b"><rect x=".5" y=".5" width="10" height="9"/><path d="M3 8V5M5.5 8V3M8 8V6"/></svg>Pie 1</h2>
    <svg class="chart" width="200" height="261" viewBox="0 0 213 278">
      <g transform="rotate(-90 121 155)" fill="none">
        <circle cx="121" cy="155" r="66.5" stroke="#e6e6e6" stroke-width="31" stroke-dasharray="87.7 417.8" stroke-dashoffset="-330.1"/>
        <circle cx="121" cy="155" r="66.5" stroke="#fb4b5c" stroke-width="31" stroke-dasharray="58.5 417.8" stroke-dashoffset="-271.6"/>
        <circle cx="121" cy="155" r="66.5" stroke="#5e9ab8" stroke-width="31" stroke-dasharray="104.5 417.8" stroke-dashoffset="-167.1"/>
        <circle cx="121" cy="155" r="68" stroke="#7fb241" stroke-width="34" stroke-dasharray="167.1 427.3"/>
      </g>
    </svg>
    <div class="legend">
      <div class="item"><b><i style="background:var(--green)"></i>40%</b><span>Visits</span></div>
      <div class="item"><b><i style="background:var(--blue-series)"></i>25%</b><span>Sales</span></div>
      <div class="item"><b><i style="background:var(--red)"></i>14%</b><span>Members</span></div>
    </div>
  </section>

  <div class="table-head" style="left:179px;width:485px">
    <h3><span class="grid-icon"><i></i><i></i><i></i><i></i><i></i><i></i></span>Table</h3>
    <div class="entries"><span>Show Entries</span><span>3 &#8661;</span></div>
  </div>
  <table class="data-table" style="left:179px;width:485px">
    <colgroup><col style="width:121px"><col style="width:119px"><col style="width:126px"><col></colgroup>
    <tr><th>Name<span>&#9660;</span></th><th>Position<span>&#9660;</span></th><th>Start Date<span>&#9660;</span></th><th>Salary<span>&#9660;</span></th></tr>
    <tr><td>John Doe</td><td>Businessman</td><td>23 Jul 2013</td><td>$32000</td></tr>
    <tr><td>John Doe</td><td>Businessman</td><td>10 Aug 2013</td><td>$11000</td></tr>
    <tr><td>John Doe</td><td>Businessman</td><td>15 Sep 2013</td><td>$45000</td></tr>
    <tr><td>John Doe</td><td>Businessman</td><td>30 Oct 2013</td><td>$4,200</td></tr>
    <tr><td>John Doe</td><td>Businessman</td><td>1 Nov 2013</td><td>$1,050</td></tr>
  </table>
  <nav class="pager" style="left:488px"><span>&lsaquo;</span><span>1</span><span>2</span><span class="on">3</span><span>4</span><span>5</span><span>6</span><span>&rsaquo;</span></nav>

  <div class="table-head" style="left:685px;width:486px">
    <h3><span class="grid-icon"><i></i><i></i><i></i><i></i><i></i><i></i></span>Table</h3>
    <div class="entries"><span>Show Entries</span><span>3 &#8661;</span></div>
  </div>
  <table class="data-table" style="left:685px;width:486px">
    <colgroup><col style="width:121px"><col style="width:119px"><col style="width:126px"><col></colgroup>
    <tr><th>Name<span>&#9660;</span></th><th>Position<span>&#9660;</span></th><th>Start Date<span>&#9660;</span></th><th>Salary<span>&#9660;</span></th></tr>
    <tr><td>John Doe</td><td>Businessman</td><td>23 Jul 2013</td><td>$32000</td></tr>
    <tr><td>John Doe</td><td>Businessman</td><td>10 Aug 2013</td><td>$11000</td></tr>
    <tr><td>John Doe</td><td>Businessman</td><td>15 Sep 2013</td><td>$45000</td></tr>
    <tr><td>John Doe</td><td>Businessman</td><td>30 Oct 2013</td><td>$4,200</td></tr>
    <tr><td>John Doe</td><td>Businessman</td><td>1 Nov 2013</td><td>$1,050</td></tr>
  </table>
  <nav class="pager" style="left:994px"><span>&lsaquo;</span><span>1</span><span>2</span><span class="on">3</span><span>4</span><span>5</span><span>6</span><span>&rsaquo;</span></nav>

  <footer class="footer">2014 &copy; Company Name. All Rights Reserved.</footer>
</div>
</body>
</html>
```